Creative Stationary for Solo Law Firm

I am looking for stationary designs for my solo law firm called TM Halvorsen Law PLLC. My logo is attached. I'd like the logo incorporated into the design.

I'm looking for a stationary design that is a bit outside of the box and not too standard or boring. The final design should communicate professionalism.

Target Market(s)

United States Clients, Opposing Counsel

Industry/Entity Type

Legal

Font styles to use
Sans Serif

Requirements
Must have
• The stationary design must incorporate my logo design attached. The design itself must be creative. The envelope design must follow standard United States designs with room for the postage stamp at the top right corner and space for the recipient's address in the middle.

```html
<!DOCTYPE html>
<html lang="en">
<head>
<meta charset="utf-8">
<title>TM Halvorsen Law PLLC – Business Cards</title>
<link rel="stylesheet" href="https://fonts.googleapis.com/css2?family=Cormorant+Garamond:wght@400;500&family=Open+Sans:wght@400&display=swap">
<style>
  :root {
    --navy: #0e2a6e;
    --ink: #1d2f6a;
    --muted: #5b6170;
    --silver: #d9dbe2;
    --rule: #c8cad0;
    --paper: #ffffff;
    --backdrop: #e9e6e1;
  }
  * { box-sizing: border-box; margin: 0; padding: 0; }
  html, body { width: 1200px; height: 950px; overflow: hidden; }
  body {
    background: var(--backdrop);
    display: flex;
    flex-direction: column;
    align-items: center;
    justify-content: center;
    gap: 70px;
  }
  .card {
    width: 630px;
    height: 360px;
    position: relative;
    overflow: hidden;
    box-shadow: 0 6px 18px rgba(0,0,0,0.18);
  }

  /* Front */
  .card-front { background: var(--paper); }
  .card-header {
    position: absolute;
    left: 56px;
    right: 40px;
    top: 0;
    height: 168px;
    display: flex;
    justify-content: space-between;
    align-items: flex-end;
    padding-bottom: 34px;
    gap: 24px;
  }
  .firm-name {
    font-family: "Cormorant Garamond", serif;
    font-variant: small-caps;
    font-weight: 500;
    font-size: 38px;
    line-height: 1;
    letter-spacing: 1px;
    color: var(--ink);
    white-space: nowrap;
  }
  .address {
    align-self: flex-start;
    margin-top: 62px;
    text-align: right;
    font-family: "Open Sans", sans-serif;
    font-size: 13px;
    line-height: 1.6;
    color: var(--muted);
    white-space: nowrap;
  }
  .divider {
    position: absolute;
    left: 56px;
    right: 40px;
    top: 168px;
    height: 1px;
    background: var(--rule);
  }
  .person {
    position: absolute;
    left: 56px;
    top: 190px;
  }
  .person-name {
    font-family: "Cormorant Garamond", serif;
    font-size: 24px;
    letter-spacing: 2px;
    text-transform: uppercase;
    color: var(--ink);
  }
  .person-title {
    font-family: "Cormorant Garamond", serif;
    font-size: 16px;
    letter-spacing: 1px;
    text-transform: uppercase;
    color: var(--muted);
    margin-bottom: 10px;
  }
  .contact-list { list-style: none; }
  .contact-list li {
    display: flex;
    align-items: center;
    gap: 10px;
    font-family: "Open Sans", sans-serif;
    font-size: 13px;
    line-height: 21px;
    color: var(--muted);
  }
  .contact-list svg { width: 12px; height: 12px; fill: var(--navy); flex: none; }

  /* Back */
  .card-back { background: var(--navy); }
  .back-web {
    position: absolute;
    left: 44px;
    top: 50%;
    transform: translate(-50%, -50%) rotate(-90deg);
    font-family: "Open Sans", sans-serif;
    font-size: 12px;
    letter-spacing: 5px;
    text-transform: uppercase;
    color: var(--silver);
    white-space: nowrap;
  }
  .back-name {
    position: absolute;
    inset: 0;
    display: flex;
    align-items: center;
    justify-content: center;
    font-family: "Cormorant Garamond", serif;
    font-weight: 400;
    font-size: 46px;
    letter-spacing: 1px;
    color: var(--silver);
  }
</style>
</head>
<body>
  <section class="card card-front" aria-label="Business card front">
    <div class="card-header">
      <div class="firm-name">TM Halvorsen Law</div>
      <div class="address">2140 Birchwood Road<br>Juneau, Alaska 99801</div>
    </div>
    <div class="divider"></div>
    <div class="person">
      <div class="person-name">Daniel Reeve</div>
      <div class="person-title">CEO/Founder</div>
      <ul class="contact-list">
        <li><svg viewBox="0 0 16 16" aria-hidden="true"><path d="M3.5 1.5l2.5 0 1 3.5-1.6 1.2a9 9 0 0 0 4.4 4.4L11 9l3.5 1v2.5c0 1-1 2-2 2C6.9 14.5 1.5 9.1 1.5 3.5c0-1 1-2 2-2z"/></svg>555 214 0387</li>
        <li><svg viewBox="0 0 16 16" aria-hidden="true"><path d="M4 1h8v14H4zM5.5 2.5v9h5v-9z"/></svg>555 730 6612</li>
        <li><svg viewBox="0 0 16 16" aria-hidden="true"><path d="M1 3h14v10H1zM2.5 4.5v.4L8 9l5.5-4.1v-.4z"/></svg>office@tmhalvorsen.com</li>
        <li><svg viewBox="0 0 16 16" aria-hidden="true"><circle cx="8" cy="8" r="7"/></svg>www.tmhalvorsen.com</li>
      </ul>
    </div>
  </section>

  <section class="card card-back" aria-label="Business card back">
    <div class="back-web">www.tmhalvorsen.com</div>
    <div class="back-name">TM Halvorsen Law</div>
  </section>
</body>
</html>
```